HOME IMPROVEMENT Business Card

I want a very unique business card. nothing typical and boring. Im open to you ideas. Ive seen cards with gold and silver or color foil and spot UV coatings. Im looking for something that looks cool and grabs attention. I like rounded corners but am open to all suggestions. We are a home improvement company and I will have a presentation folder printed and a catalog printed also and want to keep that same theme. I love the colors in our logo but I am open at looking at a 3rd color that would work with my logo. I hope that helps.
Card should include
Address
Phone
Fax
Email
Website
Target Market(s)
Home owners, people looking to remodel their home
Industry/Entity Type
Home Improvement
Contact Information for Business Card
2873 Maple Crest Avenue Unit 410
Des Plaines, Il 60284
Phone
Direct Line
Email
Website
Font styles to use
Other font styles liked:
- IM OPEN MINDED
Requirements
Must have
- High end quality look nothing boring I like rounded corners but am open minded
Nice to have
- WOW. I want something nice and impressive.
Should not have
- ??? Not sure

```html
<!DOCTYPE html>
<html lang="en">
<head>
<meta charset="utf-8">
<title>Brightwall Remodeling – Business Card</title>
<link href="https://fonts.googleapis.com/css2?family=Open+Sans:wght@400;600;800&display=swap" rel="stylesheet">
<style>
  :root{
    --bg:#e9e7e4;
    --card:#ffffff;
    --navy:#16214f;
    --green:#1f9a4a;
    --tile:#e4e4e4;
    --text:#2a2a2a;
  }
  *{margin:0;padding:0;box-sizing:border-box}
  html,body{width:1200px;height:1200px;overflow:hidden;background:var(--bg)}
  body{font-family:"Open Sans",Arial,sans-serif;position:relative}
  .card{
    position:absolute;left:150px;width:900px;height:514px;
    background:var(--card);border-radius:8px;overflow:hidden;
    box-shadow:0 10px 30px rgba(0,0,0,.18);
  }
  .card--back{top:56px}
  .card--front{top:630px}
  .tile-field{position:absolute}
  .card--back .tile-field--top{left:0;top:0;width:900px;height:230px;
    background:linear-gradient(180deg,rgba(220,220,220,.9),rgba(235,235,235,.35) 70%,rgba(255,255,255,0))}
  .card--back .tile-field--right{right:0;top:230px;width:420px;height:120px;
    background:linear-gradient(90deg,rgba(255,255,255,0),rgba(230,230,230,.7))}
  .card--front .tile-field--left{left:0;top:0;width:380px;height:300px;
    background:linear-gradient(135deg,rgba(222,222,222,.9),rgba(255,255,255,0) 75%)}
  .card--front .tile-field--right{right:0;top:0;width:360px;height:514px;
    background:linear-gradient(270deg,rgba(222,222,222,.9),rgba(255,255,255,0) 85%)}
  .contact{position:absolute;list-style:none}
  .contact li{display:flex;align-items:center;gap:16px;margin-bottom:22px;
    font-size:20px;color:var(--text);letter-spacing:.3px}
  .contact li.strong{font-weight:600}
  .contact--main{left:120px;top:300px}
  .contact--office{left:500px;top:150px}
  .contact .lines{line-height:1.3}
  .icon{width:34px;height:34px;flex:none}
  .brand{position:absolute;left:0;right:0;top:215px;display:flex;
    justify-content:center;align-items:center;gap:18px}
  .brand__mark{width:30px;height:30px;background:var(--green);border-radius:4px}
  .brand__name{font-weight:800;font-size:58px;color:var(--navy);letter-spacing:.5px}
</style>
</head>
<body>

<section class="card card--back" aria-label="Card back with contact details">
  <div class="tile-field tile-field--top" role="img" aria-label="Light grey tile grid pattern"></div>
  <div class="tile-field tile-field--right" role="img" aria-label="Light grey tile grid pattern"></div>

  <ul class="contact contact--office">
    <li>
      <svg class="icon" viewBox="0 0 34 34" aria-hidden="true"><circle cx="17" cy="17" r="17" fill="var(--navy)"/><rect x="10" y="14" width="14" height="9" rx="1.5" fill="#fff"/><rect x="12" y="9" width="10" height="6" fill="#fff"/><rect x="12" y="17" width="10" height="1.5" fill="var(--navy)"/></svg>
      <span>+18 6104 2957 3316</span>
    </li>
    <li>
      <svg class="icon" viewBox="0 0 34 34" aria-hidden="true"><circle cx="17" cy="17" r="17" fill="var(--navy)"/><path d="M17 8a6 6 0 0 1 6 6c0 5-6 12-6 12s-6-7-6-12a6 6 0 0 1 6-6z" fill="#fff"/><circle cx="17" cy="14" r="2.3" fill="var(--navy)"/></svg>
      <span class="lines">2873 Maple Crest Avenue Unit 410<br>Des Plaines, Il 60284</span>
    </li>
  </ul>

  <ul class="contact contact--main">
    <li class="strong">
      <svg class="icon" viewBox="0 0 34 34" aria-hidden="true"><circle cx="17" cy="17" r="17" fill="var(--navy)"/><path d="M11 10c1-1 2-1 3 0l2 3c.5 1 0 2-1 2.5 1 2 2.5 3.5 4.5 4.5.5-1 1.5-1.5 2.5-1l3 2c1 1 1 2 0 3-2 2-5 2-8-1s-6-6-7-9c-.5-2 0-3 1-4z" fill="#fff"/></svg>
      <span>+18 5520 3391 48</span>
    </li>
    <li>
      <svg class="icon" viewBox="0 0 34 34" aria-hidden="true"><circle cx="17" cy="17" r="17" fill="var(--navy)"/><rect x="9" y="11" width="16" height="12" rx="1" fill="#fff"/><path d="M9 11l8 7 8-7" fill="none" stroke="var(--navy)" stroke-width="1.6"/></svg>
      <span>INFO@COMPANYNAME.COM</span>
    </li>
    <li>
      <svg class="icon" viewBox="0 0 34 34" aria-hidden="true"><circle cx="17" cy="17" r="17" fill="var(--navy)"/><circle cx="17" cy="17" r="8" fill="none" stroke="#fff" stroke-width="1.6"/><ellipse cx="17" cy="17" rx="3.5" ry="8" fill="none" stroke="#fff" stroke-width="1.4"/><line x1="9" y1="17" x2="25" y2="17" stroke="#fff" stroke-width="1.4"/></svg>
      <span>WWW.COMPANY.NAME.COM</span>
    </li>
  </ul>
</section>

<section class="card card--front" aria-label="Card front with company name">
  <div class="tile-field tile-field--left" role="img" aria-label="Light grey tile grid pattern"></div>
  <div class="tile-field tile-field--right" role="img" aria-label="Light grey tile grid pattern"></div>
  <div class="brand">
    <span class="brand__mark" aria-hidden="true"></span>
    <span class="brand__name">Brightwall Remodeling</span>
  </div>
</section>

</body>
</html>
```